Banner Ad Design Project

hi i need several banner for a casino website
for examples you can visit some of the online casinos on the net.

the banners i need:

1. sportsbook
2. live casino
3. blackjack
4. slot games
5. bonus (e.g. Christmass bonus "double your deposit!" or "free spins"
6. "Do you want to win a trip to Las Vegas? Join now!"

if possible with some movement (flash/html5)

i have updated the prices!

payment committed! 

Reason: Error by brieflane End day was similar on start day

Industry/Entity Type

Casino

```html
<!DOCTYPE html>
<html lang="en">
<head>
<meta charset="utf-8">
<title>Christmas Bonus Banner</title>
<link rel="stylesheet" href="https://fonts.googleapis.com/css2?family=Roboto+Condensed:ital,wght@1,800;1,900&display=swap">
<style>
  :root {
    --bg-dark: #3a120c;
    --bg-warm: #7a2a18;
    --bg-glow: #b4562a;
    --promo-red: #e0141b;
    --promo-red-deep: #b30a10;
    --promo-white: #ffffff;
    --santa-red: #d8262a;
    --santa-cream: #f2e6d8;
  }
  html, body {
    margin: 0;
    padding: 0;
    width: 1200px;
    height: 148px;
    overflow: hidden;
    background: var(--bg-dark);
  }
  .banner {
    position: relative;
    width: 1200px;
    height: 148px;
    overflow: hidden;
  }
  .banner__backdrop {
    position: absolute;
    inset: 0;
    background:
      radial-gradient(ellipse 260px 120px at 120px 70px, rgba(190, 70, 50, 0.85), transparent 70%),
      radial-gradient(ellipse 300px 110px at 620px 90px, rgba(180, 90, 40, 0.6), transparent 70%),
      linear-gradient(90deg, var(--bg-warm) 0%, var(--bg-dark) 30%, var(--bg-glow) 60%, var(--bg-dark) 85%, var(--bg-warm) 100%);
    filter: blur(2px);
  }
  .banner__headline {
    position: absolute;
    left: 262px;
    top: 2px;
    width: 600px;
    margin: 0;
    font-family: "Roboto Condensed", "Arial Narrow", sans-serif;
    font-style: italic;
    font-weight: 900;
    font-size: 56px;
    line-height: 62px;
    color: var(--promo-white);
    text-align: center;
    letter-spacing: 0.5px;
    -webkit-text-stroke: 12px var(--promo-red);
    paint-order: stroke fill;
    text-shadow: 0 2px 0 var(--promo-red-deep);
  }
  .banner__headline span { display: block; }
  .banner__headline .headline__line--second { margin-left: 6px; }
  .snowflake-badge {
    position: absolute;
    left: 220px;
    top: 24px;
    width: 42px;
    height: 42px;
  }
  .santa-illustration {
    position: absolute;
    right: 0;
    top: 0;
    width: 320px;
    height: 148px;
    background:
      radial-gradient(ellipse 90px 80px at 230px 90px, var(--santa-cream), transparent 75%),
      radial-gradient(ellipse 120px 70px at 110px 50px, var(--santa-red), transparent 75%),
      linear-gradient(90deg, transparent 0%, rgba(216, 38, 42, 0.35) 40%, rgba(242, 230, 216, 0.5) 100%);
  }
</style>
</head>
<body>
  <div class="banner">
    <div class="banner__backdrop" role="img" aria-label="Blurred roulette wheel with red and black pockets"></div>

    <svg class="snowflake-badge" viewBox="0 0 42 42" aria-hidden="true">
      <circle cx="21" cy="21" r="20" fill="var(--promo-red)"/>
      <g stroke="var(--promo-white)" stroke-width="3" stroke-linecap="round">
        <line x1="21" y1="7" x2="21" y2="35"/>
        <line x1="8.9" y1="14" x2="33.1" y2="28"/>
        <line x1="8.9" y1="28" x2="33.1" y2="14"/>
      </g>
    </svg>

    <h1 class="banner__headline">
      <span class="headline__line--first">Christmass bonus</span>
      <span class="headline__line--second">double your deposit!</span>
    </h1>

    <div class="santa-illustration" role="img" aria-label="Cartoon Santa Claus carrying a sack of wrapped gifts"></div>
  </div>
</body>
</html>
```